Utility Contractor looking for a new website

Water and wastewater utility contractor looking to create a new website that highlights our various services. We are looking for modern web presence that can be updated with current projects and new services as we grow. We have an existing logo that we would like to incorporate into the overall design of the site
Updates

Hi, Thank you for all the design submissions. I have had some time to review and have eliminated the ones I feel are not what I am looking for. Based on the designs that remain, I am looking for a clean (not to many bold colours), modern look that is not to busy (long scrolling page), Thanks, Dean

Target Market(s)

project managers, strata boards, owners, people who make decisions as to who operates their water/wastewater system

Industry/Entity Type

Utility

Font styles to use
Sans Serif

Requirements
Must have
• A min page that describes the company and what we do, A page for each of our services that outlines the service and the benefits of it. the look must be consistent throughout. additionally each service page should have some images related to the service

```html
<!DOCTYPE html>
<html lang="en">
<head>
<meta charset="utf-8">
<title>Clearbrook Utility Works Ltd</title>
<link href="https://fonts.googleapis.com/css2?family=Titillium+Web:wght@400;600;700&family=Open+Sans:wght@400;600;700&display=swap" rel="stylesheet">
<style>
:root{
  --blue:#1a6bb5;
  --blue-dark:#15599a;
  --ink:#222;
  --text:#777;
  --muted:#999;
  --white:#fff;
  --gray-bg:#f1f1f1;
  --card:#fff;
  --hero-a:#6f7a72;
  --hero-b:#4b4f4a;
}
*{margin:0;padding:0;box-sizing:border-box}
html,body{width:1200px;height:3020px;overflow:hidden;background:var(--white)}
body{position:relative;font-family:"Open Sans",Arial,sans-serif;color:var(--ink)}
.site-header{position:absolute;top:0;left:0;width:1200px;height:50px;background:var(--white);display:flex;align-items:center;justify-content:space-between;padding:0 40px 0 44px}
.brand{display:flex;align-items:center;gap:8px;font-family:"Titillium Web",sans-serif;font-weight:700;font-size:22px;color:var(--blue-dark);letter-spacing:.5px}
.brand-mark{width:12px;height:12px;border-radius:50%;background:var(--blue)}
.main-nav{display:flex;gap:34px;font-size:12px;letter-spacing:1.5px;color:#555;text-transform:uppercase}
.hero{position:absolute;top:50px;left:0;width:1200px;height:798px;background:linear-gradient(180deg,#8c9488 0%,var(--hero-a) 35%,var(--hero-b) 100%);text-align:center;color:var(--white)}
.hero-title{position:absolute;top:258px;left:0;width:100%;font-family:"Titillium Web",sans-serif;font-weight:700;font-size:80px;line-height:86px;letter-spacing:2px;text-shadow:0 2px 6px rgba(0,0,0,.35)}
.hero-sub{position:absolute;top:452px;left:0;width:100%;font-size:36px;text-shadow:0 2px 4px rgba(0,0,0,.35)}
.hero-btn{position:absolute;top:540px;left:502px;width:196px;height:44px;border:2px solid var(--white);display:flex;align-items:center;justify-content:center;font-size:13px;letter-spacing:2px}
.hero-arrow{position:absolute;top:412px;width:20px;height:30px}
.hero-arrow.left{left:12px}.hero-arrow.right{right:12px}
.hero-bar{position:absolute;top:843px;left:133px;width:932px;height:6px;background:var(--blue)}
.what-we-do{position:absolute;top:848px;left:0;width:1200px;height:760px;text-align:center}
.section-title{font-family:"Titillium Web",sans-serif;font-weight:700;font-size:38px;letter-spacing:4px;color:var(--ink)}
.what-we-do .section-title{position:absolute;top:90px;width:100%}
.rule{position:absolute;top:184px;left:495px;width:210px;height:2px;background:#bbb}
.intro{position:absolute;top:218px;left:140px;width:920px;font-size:23px;line-height:39px;color:var(--text)}
.service{position:absolute;top:389px;width:360px;text-align:center}
.service-icon{margin:0 auto;width:115px;height:115px;border:3px solid var(--blue);display:flex;align-items:center;justify-content:center}
.service h3{margin-top:44px;font-weight:400;font-size:24px;color:var(--blue)}
.service p{margin-top:6px;font-size:13px;line-height:20px;color:var(--muted)}
.read-more{display:block;margin-top:24px;font-size:13px;color:#888}
.gallery{position:absolute;top:1608px;left:0;width:1200px;height:1118px;background:var(--gray-bg)}
.gallery .section-title{position:absolute;top:88px;width:100%;text-align:center;font-size:28px;letter-spacing:4px}
.filters{position:absolute;top:196px;width:100%;display:flex;justify-content:center;gap:24px;font-size:14px;color:#777}
.filters .active{color:var(--ink);font-weight:700}
.project{position:absolute;width:345px;height:322px;background:var(--card)}
.project-photo{height:246px;border-bottom:4px solid var(--blue)}
.project h4{margin-top:20px;text-align:center;font-size:13px;letter-spacing:1.5px;font-weight:700;color:var(--ink)}
.project span{display:block;text-align:center;font-size:12px;color:var(--muted);margin-top:2px}
.site-footer{position:absolute;top:2726px;left:0;width:1200px;height:294px;background:var(--blue);text-align:center;color:var(--white)}
.to-top{position:absolute;top:0;left:582px;width:36px;height:36px;background:#111;display:flex;align-items:center;justify-content:center}
.social{position:absolute;top:90px;left:0;width:100%;display:flex;justify-content:center;gap:14px}
.social span{width:36px;height:36px;border:1px solid rgba(255,255,255,.6)}
.footer-text{position:absolute;top:172px;width:100%;font-size:13px;line-height:24px}
</style>
</head>
<body>
<header class="site-header">
  <div class="brand"><span class="brand-mark"></span>CLEARBROOK UTILITY WORKS LTD</div>
  <nav class="main-nav"><span>Home</span><span>About</span><span>Services</span><span>Projects</span><span>Contact</span></nav>
</header>

<section class="hero" role="img" aria-label="Photo of a utility worker beside a service truck flushing a water main in a residential street">
  <svg class="hero-arrow left" viewBox="0 0 20 30"><path d="M15 5 L5 15 L15 25" fill="none" stroke="#fff" stroke-width="3"/></svg>
  <svg class="hero-arrow right" viewBox="0 0 20 30"><path d="M5 5 L15 15 L5 25" fill="none" stroke="#fff" stroke-width="3"/></svg>
  <h1 class="hero-title">UTILITY OPERATOR &amp;<br>CONTRACTOR</h1>
  <p class="hero-sub">Design. Construction. Operation. Maintenance.</p>
  <div class="hero-btn">VIEW OUR SERVICES</div>
</section>
<div class="hero-bar"></div>

<section class="what-we-do">
  <h2 class="section-title">WHAT WE DO</h2>
  <div class="rule"></div>
  <p class="intro">Water and wastewater utility contractor looking to create a new website that highlights our various services. We are looking for modern web presence that can be updated with current projects and new services as we grow.</p>

  <div class="service" style="left:38px">
    <div class="service-icon"><svg width="44" height="44" viewBox="0 0 44 44" fill="none" stroke="#1a6bb5" stroke-width="3"><circle cx="14" cy="8" r="4"/><circle cx="14" cy="36" r="4"/><circle cx="30" cy="10" r="4"/><path d="M14 12 V32 M30 14 C30 24 14 20 14 30"/></svg></div>
    <h3>System Operation</h3>
    <p>Lorem ipsum dolor sit amet, consectetur adipiscing<br>elit. Nullam ornare sem sit amet mauris.</p>
    <span class="read-more">Read more ›</span>
  </div>
  <div class="service" style="left:420px">
    <div class="service-icon"><svg width="44" height="44" viewBox="0 0 44 44"><path d="M30 6 a9 9 0 0 0 -8 12 L7 33 a3.5 3.5 0 0 0 5 5 L27 23 a9 9 0 0 0 12 -8 l-6 5 -5 -1 -1 -5 z" fill="#1a6bb5"/></svg></div>
    <h3>Fire Hydrant Maintenance</h3>
    <p>Lorem ipsum dolor sit amet, consectetur adipiscing<br>elit. Nullam ornare sem sit amet mauris.</p>
    <span class="read-more">Read more ›</span>
  </div>
  <div class="service" style="left:802px">
    <div class="service-icon"><svg width="48" height="44" viewBox="0 0 48 44" fill="none" stroke="#1a6bb5" stroke-width="4"><path d="M4 12 H14 C24 12 24 32 34 32 H42 M4 32 H14 C18 32 20 28 22 24 M26 18 C28 14 30 12 34 12 H42"/><path d="M38 6 L44 12 L38 18 M38 26 L44 32 L38 38" stroke-width="3"/></svg></div>
    <h3>Backflow Device Testing</h3>
    <p>Lorem ipsum dolor sit amet, consectetur adipiscing<br>elit. Nullam ornare sem sit amet mauris.</p>
    <span class="read-more">Read more ›</span>
  </div>
</section>

<section class="gallery">
  <h2 class="section-title">GALLERY OF PROJECTS</h2>
  <div class="filters"><span class="active">All Categories</span><span>System Operation</span><span>Fire Hydrant Maintenance</span><span>Backflow Device Testing</span></div>

  <article class="project" style="left:48px;top:265px"><div class="project-photo" role="img" aria-label="Excavation site cleanup after installation" style="background:linear-gradient(180deg,#9fb8d0,#7a6a55)"></div><h4>CLEAN UP AFTER INSTALLATION</h4><span>Read more</span></article>
  <article class="project" style="left:428px;top:265px"><div class="project-photo" role="img" aria-label="Newly installed hydrant on a lawn" style="background:linear-gradient(180deg,#c9ccc8,#4f7a35)"></div><h4>NEW HYDRANT INSTALLED</h4><span>Read more</span></article>
  <article class="project" style="left:808px;top:265px"><div class="project-photo" role="img" aria-label="Worker finishing concrete over rebar grid" style="background:linear-gradient(180deg,#8a8f7a,#4a4d52)"></div><h4>CONCRETE FINISHING</h4><span>Read more</span></article>
  <article class="project" style="left:48px;top:624px"><div class="project-photo" role="img" aria-label="Spring water main flushing from a hydrant onto the street" style="background:linear-gradient(180deg,#aab4bd,#6d716c)"></div><h4>SPRING WATER MAIN FLUSHING</h4><span>Read more</span></article>
  <article class="project" style="left:428px;top:624px"><div class="project-photo" role="img" aria-label="Blue valve assembly with new copper piloting" style="background:linear-gradient(180deg,#5d6c75,#2f4f8a)"></div><h4>REPLACING THE OLD COPER PILOTING</h4><span>Read more</span></article>
  <article class="project" style="left:808px;top:624px"><div class="project-photo" role="img" aria-label="Blue pipe laid on a forested mountain construction site" style="background:linear-gradient(180deg,#b9c2c6,#6b6650)"></div><h4>54 METER CONTACT CHAMBER</h4><span>Read more</span></article>
</section>

<footer class="site-footer">
  <div class="to-top"><svg width="14" height="10" viewBox="0 0 14 10"><path d="M1 9 L7 2 L13 9" fill="#fff"/></svg></div>
  <div class="social"><span></span><span></span><span></span><span></span><span></span><span></span></div>
  <p class="footer-text">Clearbrook Utility Works<br>© Copyrights 2014</p>
</footer>
</body>
</html>
```